Tax Preparation flyer for LedgerWise Corp.

My Client would like a one page PDF flyer to promote upcoming tax season in Canada. This firm is affordable and all virtual. I have attached a copy of their logo and a word document with the proposed wording for the flyer. Please feel free to change if you have better suggestions.

Target Market(s)

individuals in canada

Colors
0054AA
0677BA
7BADD7
CADEEF
E8F1F8

```html
<!DOCTYPE html>
<html lang="en">
<head>
<meta charset="utf-8">
<title>LedgerWise Corp. – Tax Season Flyer</title>
<link rel="stylesheet" href="https://fonts.googleapis.com/css2?family=Poppins:ital,wght@0,300;0,400;0,500;0,600;0,700;1,300;1,600;1,700&family=Rubik:wght@700&display=swap">
<style>
  :root{
    --blue:#1e9ad9;
    --blue-deep:#0677BA;
    --navy:#0a1430;
    --ink:#111111;
    --white:#ffffff;
    --backdrop:#e4e4e4;
    --slate:#555a60;
  }
  *{box-sizing:border-box;margin:0;padding:0}
  html,body{width:1200px;height:1200px;overflow:hidden;background:var(--backdrop)}
  body{font-family:"Poppins",sans-serif;color:var(--ink)}
  .flyer{position:absolute;left:136px;top:0;width:928px;height:1200px;background:var(--white);overflow:hidden}
  .shapes{position:absolute;inset:0}
  .brand{position:absolute;left:58px;top:44px;font-weight:700;color:var(--blue);font-size:40px;line-height:40px;letter-spacing:-0.5px}
  .brand span{display:block}
  .headline{position:absolute;left:54px;top:188px}
  .headline .relax{font-style:italic;font-weight:700;color:var(--blue);font-size:52px;line-height:60px}
  .headline .main{font-weight:600;font-size:39px;line-height:52px;letter-spacing:-0.3px}
  .rule{position:absolute;left:54px;top:372px;width:127px;height:6px;background:var(--blue)}
  .intro{position:absolute;left:54px;top:407px;width:470px;font-size:13.6px;line-height:21.2px;font-weight:300;letter-spacing:-0.15px}
  .intro p{margin-bottom:11px}
  .intro .lines{white-space:nowrap}
  .intro strong{font-weight:600}
  .intro .note{font-style:italic;font-weight:700;letter-spacing:-0.35px;white-space:nowrap}
  .pricing-tab{position:absolute;left:590px;top:494px;color:var(--white);font-weight:700;font-size:22px;letter-spacing:1.5px}
  .price-row{position:absolute;left:575px;width:310px;color:var(--blue)}
  .price-row .label{position:absolute;left:0;top:0;padding-left:16px;font-weight:500;font-size:17.5px;line-height:23px}
  .price-row .label::before{content:"›";position:absolute;left:0;top:-2px;font-weight:700;font-size:20px}
  .price-row .amount{position:absolute;right:0;top:0;font-family:"Rubik",sans-serif;font-weight:700;font-size:27px;text-align:right}
  .price-row .per{position:absolute;right:0;top:35px;font-style:italic;font-weight:300;font-size:12.5px;line-height:17px;text-align:right}
  .row-1{top:558px}
  .row-2{top:630px}
  .price-divider{position:absolute;left:590px;top:613px;width:295px;height:2px;background:var(--blue)}
  .tips{position:absolute;left:0;top:720px;width:928px;height:136px;background:var(--blue)}
  .tip{position:absolute;top:0;height:96px;border-left:1.5px solid var(--white);padding:16px 0 0 16px;color:var(--white);font-size:14.4px;line-height:19.6px;font-weight:300;width:272px}
  .tip-1{left:54px}
  .tip-2{left:343px}
  .tip-3{left:632px}
  .tagline{position:absolute;left:0;top:866px;width:928px;text-align:center;font-style:italic;font-weight:300;font-size:22px;color:var(--blue)}
  .pitch{position:absolute;left:64px;top:910px;width:800px;text-align:center;font-weight:500;font-size:19px;line-height:30px;letter-spacing:-0.2px;white-space:nowrap}
  .pitch .soft{font-weight:300;font-size:15.5px}
  .benefits{position:absolute;left:54px;top:1060px;width:820px;list-style:none;color:var(--white);font-size:14.2px;line-height:19.5px;font-weight:300}
  .benefits li{position:relative;padding-left:11px;margin-bottom:8px}
  .benefits li::before{content:"•";position:absolute;left:0}
  .benefits em{font-weight:700}
  .contact{position:absolute;left:0;top:1152px;width:928px;height:34px;color:var(--white);font-size:17px}
  .contact .heading{position:absolute;left:214px;top:1px;font-weight:500}
  .contact .item{position:absolute;top:0;display:flex;align-items:center;gap:7px;font-weight:300;white-space:nowrap}
  .contact .email{left:372px}
  .contact .phone{left:600px}
  .contact svg{width:24px;height:24px;flex:none}
</style>
</head>
<body>
<div class="flyer">
  <svg class="shapes" width="928" height="1200" viewBox="0 0 928 1200">
    <defs>
      <radialGradient id="techGlow" cx="0.55" cy="0.5" r="0.7">
        <stop offset="0" stop-color="#2c7fd6"/>
        <stop offset="0.45" stop-color="#12346e"/>
        <stop offset="1" stop-color="#070d22"/>
      </radialGradient>
    </defs>
    <polygon points="423,0 928,0 928,490 553,490 316,159" fill="url(#techGlow)" role="img" aria-label="Photo of a hand touching a glowing network of tax icons"/>
    <polygon points="310,168 322,158 574,535 560,535" fill="var(--blue)"/>
    <polygon points="569,490 787,490 787,535 569,535" fill="var(--blue)"/>
    <polygon points="755,490 773,490 810,535 787,535" fill="var(--slate)"/>
    <rect x="0" y="901" width="928" height="299" fill="var(--ink)"/>
    <polygon points="56,901 873,901 771,1042 154,1042" fill="var(--white)"/>
    <polygon points="0,901 56,901 154,1042 136,1042 46,917 0,917" fill="var(--blue)"/>
    <polygon points="928,901 873,901 771,1042 789,1042 882,917 928,917" fill="var(--blue)"/>
    <polygon points="136,1145 791,1145 828,1200 98,1200" fill="var(--blue)"/>
  </svg>

  <div class="brand"><span>LedgerWise</span><span>Corp.</span></div>

  <div class="headline">
    <div class="relax">Relax,</div>
    <div class="main">We’ve Got Your<br>Taxes Covered!</div>
  </div>
  <div class="rule"></div>

  <div class="intro">
    <p class="lines">Our tax preparers have over 20 years experience and<br>worked both in public accounting firms as well as<br>specialized tax. Our tax services are virtual, so you don’t<br>have to take the time for a personal visit. We take care of<br>everything and can access all your tax slips from CRA website<br>directly into our tax software. <strong>All signing is done via SignFlow.</strong></p>
    <p>You can fill and submit the appropriate forms, along with all your other documents, in our secure client portal. It’s important that we understand your situation and any changes in your situation from the past year.</p>
    <p class="note">If you have a complex tax situation and would like to discuss it,<br>we can meet in virtually over MeetLink or TalkRoom</p>
  </div>

  <div class="pricing-tab">PRICING</div>
  <div class="price-row row-1">
    <div class="label">Personal Tax<br>Return</div>
    <div class="amount">$100.00</div>
  </div>
  <div class="price-divider"></div>
  <div class="price-row row-2">
    <div class="label">Add a business<br>or rental<br>schedule</div>
    <div class="amount">$125.00</div>
    <div class="per">per business or<br>rental property.</div>
  </div>

  <div class="tips">
    <div class="tip tip-1">More complex tax returns will be assessed based on the complexity of the return and you will be advised before we start.</div>
    <div class="tip tip-2">Did you fall behind in filing your income tax save 20% when you file 3 or more years with us. We can do back to 2012 for filing of tax returns.</div>
    <div class="tip tip-3">If you expect a refund, the earlier you file the sooner you will receive your refund. Our average turn around time prior to April is a couple of days.</div>
  </div>

  <div class="tagline">TODAY SO YOU CAN START TO BREATHE EASY.</div>

  <p class="pitch"><span class="soft">Imagine having your bookkeeping on auto pilot,</span> with everything always up to<br>date and available at your fingertips. Anytime. Anywhere. You’ll<br>always know exactly where you stand with your cash flow—<br>how much you have, owe, are owed, and have made.</p>

  <ul class="benefits">
    <li><em>How will you feel?</em> Calm, relaxed, and able to make good business decisions. And you’ll have more time to work on your business. In short, you’ll be able to breathe easy.</li>
    <li><em>Sound too good to be true?</em> That’s exactly how our clients feel once all their bookkeeping stresses are gone.</li>
  </ul>

  <div class="contact">
    <div class="heading">CONTACT US</div>
    <div class="item email">
      <svg viewBox="0 0 24 24" aria-hidden="true"><circle cx="12" cy="12" r="11" fill="none" stroke="#fff" stroke-width="1.4"/><rect x="6.5" y="8" width="11" height="8" rx="1" fill="none" stroke="#fff" stroke-width="1.4"/><path d="M6.5 8.5 12 12.5 17.5 8.5" fill="none" stroke="#fff" stroke-width="1.4"/></svg>
      hi@ledgerwise.ca
    </div>
    <div class="item phone">
      <svg viewBox="0 0 24 24" aria-hidden="true"><circle cx="12" cy="12" r="11" fill="none" stroke="#fff" stroke-width="1.4"/><path d="M8.6 6.8c.5-.4 1.1-.3 1.4.2l1 1.6c.3.5.2 1-.2 1.4l-.7.6c.6 1.3 1.600 2.4 2.9 3l.6-.7c.4-.4.9-.5 1.4-.2l1.6 1c.5.3.6.9.2 1.4l-.8.9c-.6.6-1.5.8-2.3.5-3.1-1.2-5.4-3.5-6.6-6.6-.3-.8-.1-1.7.5-2.3z" fill="none" stroke="#fff" stroke-width="1.3"/></svg>
      555 014 2290
    </div>
  </div>
</div>
</body>
</html>
```